依頼詳細
6月2日は感謝を伝えるペルミナの日であることが日本の当たり前の記念日になることが最終目的です。
そのためのイベント企画として、
「ありがとう」を伝えたい人、もの、コトを広く募集するためのチラシのデザインをお願いします。
主催は、一般社団法人ミルデン香木文化協会とTovelWorksです。
宣伝は、WEBと紙の両方で行います。
毎年、6月2日に発表し、受賞者に賞状をお送りする予定です。

記載項目
6月2日は感謝を伝えるペルミナの日
6月2日はペルミナの日
6月2日はありがとうを伝えるペルミナの日
日頃の感謝の思いを伝えたい人、もの、コト
ペルミナの日に発表
2020年から毎年開催!その第1回

ペルミナの日とは?
https://www.tovelworks-example.com/6-2

一般社団法人ブルガリアンローズ文化協会http://www.milden-koboku-example.or.jp/

トーベルワークス
https://www.tovelworks-example.com/

サイズ
A4
ページ数
片面
希望イメージ
シンプル 複雑
単色 カラフル
暗い 明るい
日常 高級
遊び心 厳粛
未来的 伝統的
女性的 男性的
希望する色
赤系、薔薇のイメージ
納品ファイル
• 高解像度JPG (.jpg)
• イラストレーター形式 (.ai)
• フォトショップ形式 (.psd)
• PNG形式 (.png)
補足説明
お世話になっております。
まもなく締め切りですが、たまたま本日急用ができ、このタイミングでの確認が難しい状況です。
そのままで決定的なものがないので、
若干の修正をセットで、期間修了後に決定させていただいてもよろしいでしょうか。
■ 選んだ理由

募集目的が明確に表現されていたことと、6月2日はペルミナの日であることが、この1枚でインプットされるような気がしたこと。
全体のまとまり、上品さがなども含め決め手となりましたのと、こちらの要望への対応が早かったことがとてもうれしく感じられました。

■ 提案者全員のお礼・コメント

素敵なご提案をたくさんありがとうございました。
どれもとても素晴らしく、特にいくつか最後まで迷いました。
こちらの不慣れさと不手際でご迷惑をおかけした方もいらしたと思います。
申し訳ございませんでした。
今後もお願いすることがあると思います。
どうぞよろしくお願い申し上げます。
本当にありがとうございました。

```html
<!DOCTYPE html>
<html lang="ja">
<head>
<meta charset="utf-8">
<title>6月2日はペルミナの日</title>
<link rel="stylesheet" href="https://fonts.googleapis.com/css2?family=Great+Vibes&family=Noto+Sans+JP:wght@400;700&display=swap">
<style>
  :root {
    --leaf-dark: #2f5a24;
    --leaf-mid: #5f8f3a;
    --leaf-light: #a9c98a;
    --rose-pink: #f2a9c0;
    --rose-deep: #d9386b;
    --rose-pale: #fbe3ea;
    --panel: rgba(40, 44, 50, 0.72);
    --text: #ffffff;
  }
  * { margin: 0; padding: 0; box-sizing: border-box; }
  html, body { width: 849px; height: 1200px; overflow: hidden; }
  body { font-family: "Noto Sans JP", sans-serif; color: var(--text); }

  .flyer { position: relative; width: 849px; height: 1200px; overflow: hidden; }

  .rose-photo {
    position: absolute; inset: 0;
    background:
      radial-gradient(ellipse 180px 150px at 560px 330px, var(--rose-pale), transparent 70%),
      radial-gradient(ellipse 170px 150px at 720px 380px, var(--rose-pink), transparent 72%),
      radial-gradient(ellipse 150px 130px at 330px 500px, var(--rose-pink), transparent 72%),
      radial-gradient(ellipse 180px 160px at 570px 620px, var(--rose-pink), transparent 72%),
      radial-gradient(ellipse 160px 140px at 780px 760px, var(--rose-pink), transparent 72%),
      radial-gradient(ellipse 120px 200px at 30px 700px, var(--rose-deep), transparent 72%),
      radial-gradient(ellipse 140px 120px at 650px 770px, var(--rose-deep), transparent 72%),
      radial-gradient(ellipse 300px 240px at 150px 150px, var(--leaf-light), transparent 75%),
      linear-gradient(180deg, var(--leaf-mid) 0%, var(--leaf-dark) 55%, var(--leaf-mid) 100%);
  }

  .info-panel {
    position: absolute; left: 42px; top: 560px; width: 420px; height: 606px;
    background: var(--panel);
    padding: 58px 30px 0 30px;
  }

  .event-title {
    font-family: "Great Vibes", cursive;
    font-weight: 400; font-size: 54px; line-height: 1;
  }
  .title-rule { border: 0; border-top: 1.5px solid var(--text); margin: 14px 0 20px; }

  .headline { font-size: 25px; font-weight: 700; line-height: 1.3; margin-bottom: 10px; }
  .lead { font-size: 15px; line-height: 1.72; }

  .contacts { position: absolute; left: 30px; right: 20px; top: 390px; }
  .contact { margin-bottom: 18px; font-size: 15px; line-height: 1.55; }
  .contact-url { font-size: 12.5px; letter-spacing: 0.02em; }
</style>
</head>
<body>
<main class="flyer">
  <div class="rose-photo" role="img" aria-label="緑の葉を背景に咲くピンクのバラの写真"></div>

  <section class="info-panel">
    <h1 class="event-title">Happy Permina Day</h1>
    <hr class="title-rule">
    <p class="headline">6月2日は感謝を伝えるペルミナの日</p>
    <p class="lead">日頃の感謝の思いを伝えたい人、もの、コト<br>ペルミナの日に発表<br>2020年から毎年開催！その第1回</p>

    <div class="contacts">
      <div class="contact">
        <p>ペルミナの日とは？</p>
        <p class="contact-url">https://www.tovelworks-example.com/6-2</p>
      </div>
      <div class="contact">
        <p>一般社団法人</p>
        <p>ミルデン香木文化協会</p>
        <p class="contact-url">http://www.milden-koboku-example.or.jp/</p>
      </div>
      <div class="contact">
        <p>トーベルワークス</p>
        <p class="contact-url">https://www.tovelworks-example.com/</p>
      </div>
    </div>
  </section>
</main>
</body>
</html>
```